Lanternway Circle Monthly Giving Flyer

We need a flyer to promote a monthly giving program called Lanternway Circle to support our nonprofit organization, Brightpath Youth Trust. We have a group of students from Uganda travelling across the country in a performing arts group called Voices of Korali. While they are on tour we want audience members to sign up to become monthly donors and support our ongoing educational work in Uganda. This flyer will be on the info table, in seats, and handed out throughout the course of the tour.

Lanternway Circle is a new program. The idea is that the audience members will be motivated by their interaction with the students to fill in their information to sign up to make a monthly gift. In exchange, we'll give them a free merchandise item (CD, tshirt, etc) for signing up and we'll send them special updates from the students throughout the year electronically.

Check out BrightpathYouthTrust.org for more info about our programs, Lanternway Circle and our branding/style.

This will be printed as a 5x7 two-sided postcard that we can print cheaply in color.

Side 1: Draw attention to the program graphically with a message of "Join Us Become an Lanternway Member," happy student image, etc. You can download an image from the gallery on our website, if you choose at: http://www.brightpathyouthtrust.org/who-we-are/media/ (scroll to the bottom)

Side 2: Lead in text: Join our network of friends committed to supporting the ongoing education of Brightpath scholars through monthly donations. As an Lanternway Member, you play a critical role by helping ensure that we can provide the life-changing services to our scholars month in and month out.
We'll send you special updates from the students throughout the year to keep you up to date on how your gifts are impacting lives.

I'd like to give $25, $50, $75, $100, or $____ other amount
Name, address, phone number, email
Credit card #, expiration, and security code
I've provided a voided check for monthly electronic funds transfer

Requirements
Nice to have
• We have not created a logo or done any branding for Lanternway Circle so it would be nice to have a nicely designed logo/font for Lanternway Circle incorporated into the flyer design that we can in other places as well to promote the program.
Should not have
• Anything that play on the poverty or challenges in Africa. We try to provide always positive image of Africa and the students we work with.

```html
<!DOCTYPE html>
<html lang="en">
<head>
<meta charset="utf-8">
<title>Lanternway Circle Monthly Giving Postcard</title>
<link href="https://fonts.googleapis.com/css2?family=Oswald:wght@500;700&family=Source+Sans+3:ital,wght@0,400;0,600;0,700;1,400;1,600&display=swap" rel="stylesheet">
<style>
  :root {
    --backdrop: #c9a677;
    --orange: #f26522;
    --orange-deep: #e2461f;
    --green: #2f9e45;
    --green-band: #1f9146;
    --ink: #231f20;
    --paper: #ffffff;
    --quote-band: #9c9c9c;
    --rule: #231f20;
  }
  * { box-sizing: border-box; margin: 0; padding: 0; }
  html, body { width: 1200px; height: 438px; overflow: hidden; }
  body {
    background: var(--backdrop);
    font-family: "Source Sans 3", Arial, sans-serif;
    color: var(--ink);
    position: relative;
  }

  /* Side 1 */
  .front {
    position: absolute; left: 9px; top: 11px;
    width: 568px; height: 413px;
    background: var(--paper);
    overflow: hidden;
  }
  .front__quote {
    height: 42px;
    background: linear-gradient(90deg, #8d8d8d, #b5b5b5 60%, #9a9a9a);
    color: #fff;
    font-style: italic; font-weight: 600;
    font-size: 15.5px;
    display: flex; align-items: center; justify-content: center;
    letter-spacing: 0.1px;
  }
  .front__photo {
    position: absolute; left: 0; top: 42px; right: 0; bottom: 0;
    background:
      radial-gradient(ellipse at 25% 55%, #e76b8a 0%, transparent 38%),
      radial-gradient(ellipse at 80% 60%, #d9dadb 0%, transparent 35%),
      radial-gradient(ellipse at 50% 20%, #b36a5a 0%, transparent 50%),
      linear-gradient(180deg, #a0605a 0%, #6d4a3c 45%, #5a3b30 100%);
  }
  .front__call {
    position: absolute; left: 20px; bottom: 12px;
    display: flex; align-items: baseline; gap: 10px;
  }
  .front__join {
    font-family: "Oswald", Impact, sans-serif;
    font-weight: 700; font-size: 50px; line-height: 1;
    color: var(--orange-deep);
    letter-spacing: -0.5px;
  }
  .front__become {
    font-family: "Oswald", Impact, sans-serif;
    font-weight: 500; font-size: 25px;
    color: #fbe9dd;
  }

  /* Side 2 */
  .back {
    position: absolute; left: 628px; top: 13px;
    width: 565px; height: 411px;
    background: var(--paper);
    overflow: hidden;
  }
  .back__intro {
    position: absolute; left: 22px; top: 16px; width: 228px;
    font-size: 14.6px; line-height: 1.32;
  }
  .back__intro p { margin-bottom: 19px; }
  .brand-word { color: var(--orange); font-weight: 700; }
  .brand-role { color: var(--green); font-style: italic; }

  .back__divider {
    position: absolute; left: 252px; top: 10px; height: 340px;
    border-left: 1px dotted #8a8a8a;
  }

  .pledge {
    position: absolute; left: 262px; top: 8px; width: 290px;
  }
  .pledge__kicker {
    color: var(--orange); font-weight: 700; font-size: 13.5px; letter-spacing: 0.2px;
  }
  .pledge__title {
    font-family: "Oswald", Impact, sans-serif;
    font-weight: 700; font-size: 30px; line-height: 0.95;
    color: var(--green);
  }
  .pledge__lead { font-size: 14px; margin-top: 3px; }
  .amounts { list-style: none; margin: 2px 0 6px 10px; font-size: 14px; line-height: 1.42; }
  .amounts li { display: flex; align-items: center; gap: 4px; }
  .box {
    width: 13px; height: 13px; border: 1.5px solid var(--ink); display: inline-block;
  }
  .blank { display: inline-block; width: 24px; border-bottom: 1px solid var(--ink); height: 12px; }
  .fields { font-size: 14px; line-height: 1.34; }
  .field { display: flex; align-items: flex-end; }
  .field .line { flex: 1; border-bottom: 1.5px solid var(--rule); margin: 0 6px 4px 4px; }
  .field .short { flex: 0 0 40px; }
  .check-note {
    display: flex; gap: 6px; font-size: 13.5px; line-height: 1.2; margin-top: 7px;
  }
  .check-note .box { flex: 0 0 13px; margin-top: 2px; }

  .band {
    position: absolute; left: 0; right: 0; bottom: 0; height: 58px;
    background: var(--green-band);
    color: #fff;
    display: flex; align-items: center;
  }
  .band__brand {
    display: flex; align-items: center; gap: 10px;
    padding-left: 22px; width: 255px;
    font-weight: 700; font-size: 17px;
  }
  .band__mark {
    width: 30px; height: 30px; border-radius: 50%; background: var(--orange); flex: 0 0 30px;
  }
  .band__contact {
    flex: 1; text-align: center; font-weight: 700; font-size: 14px; line-height: 1.12;
  }
  .band__web { font-size: 14.5px; }
</style>
</head>
<body>

<section class="front" aria-label="Postcard side one">
  <div class="front__quote">“Education is the most powerful weapon with which we can use to change the world.” – Amani Okoth</div>
  <div class="front__photo" role="img" aria-label="Photo of five smiling students standing together outdoors in front of a pink wall"></div>
  <div class="front__call">
    <span class="front__join">JOIN US!</span>
    <span class="front__become">Become an Lanternway Member</span>
  </div>
</section>

<section class="back" aria-label="Postcard side two">
  <div class="back__intro">
    <p>Join our network of friends committed to supporting the ongoing education of <span class="brand-word">Brightpath</span> scholars through monthly donations.</p>
    <p>As an <span class="brand-role">Lanternway Member</span>, you play a critical role by helping ensure that we can provide the life-changing services to our scholars month in and month out.</p>
    <p>We’ll send you special updates from the students throughout the year to keep you up to date on how your gifts are impacting lives.</p>
  </div>

  <div class="back__divider"></div>

  <form class="pledge">
    <div class="pledge__kicker">BECOME A DONOR</div>
    <div class="pledge__title">MAKE AN IMPACT</div>
    <div class="pledge__lead">I’d like to give:</div>
    <ul class="amounts">
      <li><span class="box"></span>$25</li>
      <li><span class="box"></span>$50</li>
      <li><span class="box"></span>$75</li>
      <li><span class="box"></span>$100</li>
      <li><span class="box"></span>$<span class="blank"></span> other amount</li>
    </ul>
    <div class="fields">
      <div class="field">Name<span class="line"></span></div>
      <div class="field">Address<span class="line"></span></div>
      <div class="field">Phone Number<span class="line"></span></div>
      <div class="field">Email<span class="line"></span></div>
      <div class="field">Credit card #<span class="line"></span></div>
      <div class="field">Expiration<span class="line short"></span>Security code<span class="line"></span></div>
    </div>
    <div class="check-note"><span class="box"></span><span>I’ve provided a voided check for<br>monthly electronic funds transfer</span></div>
  </form>

  <footer class="band">
    <div class="band__brand"><span class="band__mark"></span>Brightpath Youth Trust</div>
    <div class="band__contact">
      P.O. Box 50418<br>
      Fairhaven, TX. 75099<br>
      555.014.2738<br>
      <span class="band__web">www.BrightpathYouthTrust.org</span>
    </div>
  </footer>
</section>

</body>
</html>
```